Creative flyer for small business IT services

We are an IT services company based in Western Australia. We're looking to expand our market share amongst small businesses and need a brochure/flyer designed to give them a good overview of why we can help them. The design and layout should be consistent with an existing company profile brochure (included) but please be creative. A comprehensive brief with copy and a rough layout is included.

Small Business

```html
<!DOCTYPE html>
<html lang="en">
<head>
<meta charset="utf-8">
<title>Small Business IT Solutions – KeystoneByte</title>
<link href="https://fonts.googleapis.com/css2?family=Open+Sans:wght@400;600;700;800&display=swap" rel="stylesheet">
<style>
:root{
  --red:#d71f26;
  --ink:#3a3a3a;
  --grey:#6b6b6b;
  --bg:#5a5a5a;
  --paper:#ffffff;
  --navy:#1f3d73;
  --sky:#cfe6f3;
  --silver:#e4e4e4;
  --blue:#1d8fc9;
}
*{box-sizing:border-box;margin:0;padding:0}
html,body{width:1200px;height:1008px;overflow:hidden}
body{background:var(--bg);font-family:"Open Sans",Arial,sans-serif;color:var(--ink);position:relative}
.flyer{position:absolute;left:253px;top:14px;width:693px;height:980px;background:var(--paper);box-shadow:0 6px 24px rgba(0,0,0,.45);overflow:hidden}
.top-band{height:58px;background:var(--red);display:flex;align-items:center;justify-content:flex-end;padding-right:26px}
.top-band h2{color:#fff;font-weight:800;font-size:21px;letter-spacing:1px}
.hero-photo{position:absolute;left:0;top:64px;width:693px;height:110px;background:linear-gradient(180deg,#ffffff 0%,#eef5e6 45%,#8a5a3a 100%)}
.headline{position:absolute;right:34px;top:176px;text-align:right}
.headline h1{color:var(--red);font-size:31px;font-weight:700;letter-spacing:.5px;line-height:1.05}
.headline p{font-size:20px;color:var(--ink);margin-top:2px}
.content-box{position:absolute;left:22px;top:252px;width:649px;height:392px;border:3px solid var(--red);border-radius:20px;display:flex;padding:14px 18px;gap:22px}
.col-left{width:330px}
.col-right{flex:1;padding-top:28px}
.section-title{color:var(--red);font-size:10px;font-weight:700;text-transform:uppercase;margin:8px 0 3px}
.section-title:first-child{margin-top:0}
.lead{font-size:11.5px;margin-bottom:4px}
.red-text{color:var(--red);font-size:9.5px;line-height:1.3;margin-bottom:5px}
.why{color:var(--blue);font-style:italic;font-size:9.5px;font-weight:600;margin-bottom:2px}
.bullets{list-style:none;font-size:9.5px;line-height:1.35}
.bullets li::before{content:"";display:inline-block;width:5px;height:5px;border-radius:50%;background:var(--red);margin-right:6px;vertical-align:middle}
.small{font-size:7.5px;line-height:1.35;color:var(--grey)}
.sub-lead{font-size:12px;margin-bottom:5px}
.body{font-size:10px;line-height:1.35;margin-bottom:8px}
.blue{color:var(--blue);font-size:10.5px;font-weight:600;line-height:1.35;margin-bottom:6px}
.quote{color:var(--red);font-size:9.5px;line-height:1.35;margin-top:6px}
.quote-by{color:var(--red);font-size:9.5px;font-weight:700;font-variant:small-caps;text-align:right;margin-top:3px}
.partnerships{position:absolute;left:40px;top:660px;width:340px}
.partnerships h3{font-size:10.5px;font-weight:700;margin-bottom:3px}
.partnerships p{font-size:10px;line-height:1.4}
.badges{position:absolute;left:400px;top:660px;width:260px;height:130px}
.badge{position:absolute}
.badge-a{left:30px;top:0;width:130px;height:26px;background:var(--silver);border-radius:3px}
.badge-b{left:0;top:38px;width:95px;height:58px;background:var(--navy)}
.badge-c{left:105px;top:48px;width:50px;height:48px;background:var(--sky)}
.badge-d{left:168px;top:30px;width:88px;height:88px;background:var(--silver);border-radius:10px}
.customers{position:absolute;left:40px;top:800px;width:620px;font-size:11.5px;line-height:1.4;color:var(--ink)}
.contact-row{position:absolute;left:30px;top:834px;width:640px;height:80px;display:flex;align-items:center}
.contact-row > div{padding:0 16px;border-left:1px solid var(--red);height:56px;display:flex;flex-direction:column;justify-content:center;white-space:nowrap}
.contact-row > div:first-child{border-left:none;padding-left:0}
.brand{flex-direction:row !important;align-items:center;gap:8px;width:150px;justify-content:flex-start !important}
.brand-mark{width:18px;height:22px;background:var(--red)}
.brand-name{font-size:17px;color:var(--ink)}
.address,.web{font-size:10px;line-height:1.4}
.web strong{font-weight:700}
.phone{font-size:22px;font-weight:700;color:#222}
.bottom-band{position:absolute;left:0;bottom:0;width:693px;height:46px;background:var(--red)}
</style>
</head>
<body>
<article class="flyer">
  <header class="top-band"><h2>SMALL BUSINESS IT SOLUTIONS</h2></header>
  <div class="hero-photo" role="img" aria-label="Row of green seedlings sprouting from mounds of soil"></div>
  <div class="headline">
    <h1>SMALL BUSINESS. BIG IDEAS.</h1>
    <p>We'll help your business grow</p>
  </div>

  <section class="content-box">
    <div class="col-left">
      <h3 class="section-title">Introduction</h3>
      <p class="lead">We help small businesses get ahead of the pack.</p>
      <p class="red-text">You've always got more to do in a small business, the last thing you need is another hat to wear. You shouldn't need to become a computer engineer to keep your business running smoothly. Say goodbye to IT headaches – our mission is to make your life easier.</p>
      <p class="why">Here's why small businesses love KeystoneByte:</p>
      <ul class="bullets">
        <li>We're small business IT experts</li>
        <li>We speak plain English and won't waste your time</li>
        <li>We care about our relationships</li>
        <li>We worry about IT so you don't have to</li>
      </ul>
      <h3 class="section-title">Support Services</h3>
      <p class="small">Whether you have a single computer or a big team with complex requirements, our expert team can assist. We offer flexible plans, clear pricing and fast help from people who know your setup.</p>
      <h3 class="section-title">Monitoring &amp; Backup</h3>
      <p class="small">Most small businesses don't protect themselves from the kind of disaster that strikes every day. Our monitoring and backup service keeps watch on your systems and keeps copies of your data safe, so you can relax.</p>
      <h3 class="section-title">Hardware &amp; Software</h3>
      <p class="small">Every business needs the right tools for the job. We supply world class hardware and software products from trusted brands, and our partnerships give you real buying power.</p>
      <p class="small">From a single keyboard to an entire infrastructure, we always take the time to help you select the right products.</p>
    </div>
    <div class="col-right">
      <h3 class="section-title">Audit</h3>
      <p class="sub-lead">It helps to know where you stand</p>
      <p class="body">Get a clearer picture of your IT systems with our obligation-free IT audit and consultation.</p>
      <p class="body">Contact us today and we'll provide you with expert insights into how your business can benefit from today's amazing technology.</p>
      <h3 class="section-title">Testimonials</h3>
      <p class="blue">Don't just take our word for it! Here's what some satisfied customers have to say about KeystoneByte:</p>
      <p class="quote">• "We are pleased to have KeystoneByte as part of our team. I recommend KeystoneByte for any business seeking a trustworthy, reliable and effective IT service provider."</p>
      <p class="quote-by">Sam Reilly, Coastal Imaging</p>
      <p class="quote">• "KeystoneByte's expertise has allowed us to test, analyse and improve the reliability and performance of our application, further improving the health and financial status of our business."</p>
      <p class="quote-by">Laura Finch, Ledgerline Pty Ltd</p>
    </div>
  </section>

  <section class="partnerships">
    <h3>World Class Partnerships</h3>
    <p>We proudly work with a range of industry leaders to ensure your business is powered by the best of today's technology. With major partners including Corvantis, Halberd, Netrova, Virtuline and Sentrix, you can be confident that our solutions are built on a strong foundation.</p>
  </section>

  <div class="badges" aria-label="Partner badges">
    <div class="badge badge-a"></div>
    <div class="badge badge-b"></div>
    <div class="badge badge-c"></div>
    <div class="badge badge-d"></div>
  </div>

  <p class="customers">Our valued customers are already enjoying the benefits of partnering with KeystoneByte. Join them by contacting us today:</p>

  <footer class="contact-row">
    <div class="brand"><span class="brand-mark"></span><span class="brand-name">KeystoneByte</span></div>
    <div class="address">Level 12, 88 Harbour Lane<br>Perth WA 6000</div>
    <div class="web">sales@keystonebyte.com.au<br><strong>www.keystonebyte.com.au</strong></div>
    <div class="phone">1300 555 018</div>
  </footer>
  <div class="bottom-band"></div>
</article>
</body>
</html>
```